KVR Webpage

We are a group dedicated to Paranormal research located in central Mississippi .. we are looking for an index page and a blank template so we can fill in and finish the rest. Would like links to include, Home, About us, Research, Contact us and More.. kind of like the look of the image uploaded .. also included is our logo

Group

Coded - Design and coding required

```html
<!DOCTYPE html>
<html lang="en">
<head>
<meta charset="utf-8">
<title>KVR Paranormal</title>
<link rel="stylesheet" href="https://fonts.googleapis.com/css2?family=Jim+Nightshade&family=Lato:wght@400;700&family=Arimo&display=swap">
<style>
:root{
  --ink:#000;
  --night:#1b2a44;
  --bone:#d9d0b3;
  --bone-dark:#c8bb93;
  --tan:#cbbf93;
  --headline:#d8ccaa;
  --body-grey:#7a7a78;
  --footer:#1c1b18;
  --base:#0e0e0d;
  --light:#e8e6df;
}
*{margin:0;padding:0;box-sizing:border-box}
html,body{width:903px;height:1200px;overflow:hidden;background:var(--ink)}
.page{position:relative;width:903px;height:1200px;overflow:hidden;font-family:'Lato',sans-serif;background:var(--ink)}
.abs{position:absolute}
.hero-scene{left:0;top:0;width:903px;height:680px;background:radial-gradient(ellipse at 62% 8%,#8fa3b8 0%,#3a4e6b 18%,var(--night) 42%,#0b1220 72%,#000 100%)}
.clock-scene{left:90px;top:770px;width:520px;height:260px;background:radial-gradient(ellipse at 50% 60%,rgba(120,110,95,.35),rgba(0,0,0,0) 70%)}
.nav-band{left:0;top:24px;width:903px;height:44px;background:linear-gradient(#151a22cc,#0c0f15dd);border-bottom:1px solid #3a3d42}
.main-nav{left:336px;top:31px;width:470px;height:30px;display:flex;justify-content:space-between;align-items:center;font-family:'Jim Nightshade',cursive;font-size:17px;color:#f2ede0}
.main-nav .sep{font-family:'Lato',sans-serif;font-size:16px;color:#cfc8b6}
.brand{left:142px;top:24px;width:162px;text-align:center;color:var(--bone);font-family:'Lato',sans-serif;font-weight:700;font-size:26px;letter-spacing:2px}
.brand-dot{left:193px;top:70px;width:60px;height:60px;border-radius:50%;background:var(--bone)}
.headline{left:110px;top:334px;font-size:29px;line-height:37px;color:var(--headline);font-weight:700;letter-spacing:.2px}
.card{width:221px;height:144px;top:480px;border-radius:5px;background:linear-gradient(var(--bone),#cfc5a6)}
.card h2{position:absolute;left:12px;top:12px;font-family:'Jim Nightshade',cursive;font-weight:400;font-size:24px;color:#111}
.card p{position:absolute;left:15px;top:55px;width:196px;font-size:11px;line-height:16px;color:#3a382f}
.card .more{position:absolute;right:8px;bottom:7px;width:14px;height:14px;border-radius:2px;background:#111;color:var(--bone);font-size:13px;line-height:13px;text-align:center;font-weight:700}
.card .hood{position:absolute;right:16px;top:-38px;width:50px;height:56px;border-radius:24px 24px 8px 8px;background:linear-gradient(#d9d0b3,#2b2a26)}
.card-shine{top:627px;width:221px;height:45px;background:linear-gradient(rgba(60,58,52,.45),rgba(0,0,0,0))}
.welcome{left:99px;top:673px;font-family:'Jim Nightshade',cursive;font-size:20px;color:#8d8c88}
.welcome span{color:var(--light)}
.rule{border-top:1px dashed #4a4944}
.intro{left:99px;width:455px;font-size:11.5px;line-height:18px;color:var(--body-grey);letter-spacing:.2px}
.video{left:583px;top:674px;width:221px;height:146px;background:linear-gradient(135deg,#5a5a5a,#2c2c2c 55%,#8a8a8a)}
.video-bar{left:583px;top:820px;width:221px;height:30px;background:#1a1a1a}
.swoosh{left:0;top:900px;width:903px;height:300px}
.emblem-name{left:670px;top:935px;width:110px;text-align:center;color:var(--bone);font-weight:700;font-size:20px;letter-spacing:2px}
.emblem-dot{left:705px;top:885px;width:40px;height:40px;border-radius:50%;background:var(--bone)}
.col-title{top:1025px;font-family:'Arimo',sans-serif;font-size:14.5px;color:var(--light)}
.quick{left:100px;top:1059px;list-style:none;font-size:10px;line-height:15px;color:var(--light)}
.quick li::before{content:"›";font-weight:700;margin-right:5px}
.field{left:249px;width:169px;background:#f1f0ec;border-radius:2px;font-size:8px;color:#8a8a8a;font-style:italic;padding:3px 6px}
.submit{left:249px;top:1145px;width:50px;height:17px;background:var(--tan);border-radius:2px;font-size:8.5px;font-style:italic;color:#222;padding:3px 8px}
.news{left:441px;width:172px;font-size:9.5px;line-height:12.5px;color:var(--light)}
.news .date{color:var(--tan);font-weight:700;font-size:11px;line-height:14px}
.contact{left:652px;width:160px;font-size:9.5px;line-height:15px;color:var(--light)}
.base{left:0;top:1174px;width:903px;height:26px;background:var(--base)}
.copy{left:99px;top:1180px;font-family:'Arimo',sans-serif;font-size:9px;color:var(--light)}
.social{top:1177px;width:18px;height:18px;border-radius:2px}
</style>
</head>
<body>
<div class="page">
  <div class="abs hero-scene" role="img" aria-label="Moonlit haunted mansion behind wrought-iron cemetery gates with a glowing lantern"></div>
  <div class="abs clock-scene" role="img" aria-label="Faint antique clock face with Roman numerals"></div>

  <div class="abs nav-band"></div>
  <nav class="abs main-nav">
    <span>Home</span><span class="sep">†</span><span>About</span><span class="sep">†</span><span>Research</span><span class="sep">†</span><span>News</span><span class="sep">†</span><span>Videos</span><span class="sep">†</span><span>Contact Us</span>
  </nav>

  <div class="abs brand">KVR</div>
  <div class="abs brand-dot"></div>

  <h1 class="abs headline">Research and investigate claims<br>of paranormal activity</h1>

  <section class="abs card" style="left:99px">
    <div class="hood" role="img" aria-label="Hooded figure ornament"></div>
    <h2>About Us</h2>
    <p>Sed ut perspiciatis unde omnis iste na tus error sit voluptatem accusan tium doloremque natus error sit voluptat em accusan.</p>
    <div class="more">+</div>
  </section>
  <section class="abs card" style="left:341px">
    <div class="hood" role="img" aria-label="Hooded figure ornament"></div>
    <h2>Our Research</h2>
    <p>Sed ut perspiciatis unde omnis iste na tus error sit voluptatem accusan tium doloremque natus error sit voluptat em accusan.</p>
    <div class="more">+</div>
  </section>
  <section class="abs card" style="left:584px">
    <div class="hood" role="img" aria-label="Hooded figure ornament"></div>
    <h2>Haunted Places</h2>
    <p>Sed ut perspiciatis unde omnis iste na tus error sit voluptatem accusan tium doloremque natus error sit voluptat em accusan.</p>
    <div class="more">+</div>
  </section>
  <div class="abs card-shine" style="left:99px"></div>
  <div class="abs card-shine" style="left:341px"></div>
  <div class="abs card-shine" style="left:584px"></div>

  <h2 class="abs welcome">Welcome to <span>KVR Paranormal Investigations</span></h2>
  <div class="abs rule" style="left:99px;top:705px;width:455px"></div>
  <p class="abs intro" style="top:712px">Sed ut perspiciatis unde omnis iste natus error sit voluptatem accusantium doloremque laudantium, totam rem aperiam, eaque ipsa quae ab illo inventore veritatis et quasi architecto beatae vitae dicta sunt explicabo. Nemo enim ipsam voluptatem quia voluptas sit aspernatur aut odit aut voluptas sit aspernatur aut odit aut fugit.</p>
  <p class="abs intro" style="top:803px">Totam rem aperiam, eaque ipsa quae ab illo inventore veritatis et quasi architecto beatae vitae dicta sunt explicabo.</p>

  <div class="abs video" role="img" aria-label="Black and white investigation video still of a dim room"></div>
  <div class="abs video-bar">
    <svg width="221" height="30" viewBox="0 0 221 30">
      <rect x="12" y="11" width="2" height="8" fill="#fff"/><rect x="16" y="11" width="2" height="8" fill="#fff"/>
      <rect x="29" y="14" width="90" height="2" fill="#555"/><rect x="29" y="14" width="32" height="2" fill="#d42020"/>
      <circle cx="61" cy="15" r="4" fill="#eee"/>
      <rect x="138" y="10" width="9" height="10" fill="none" stroke="#999"/>
      <rect x="160" y="9" width="32" height="12" rx="6" fill="#2a2a2a"/><circle cx="167" cy="15" r="6" fill="#ddd"/>
    </svg>
  </div>

  <svg class="abs swoosh" viewBox="0 0 903 300" aria-hidden="true">
    <path d="M0 36 C150 90 300 130 420 112 C540 96 640 60 700 45 L903 20 L903 300 L0 300 Z" fill="var(--tan)"/>
    <path d="M0 50 C150 104 300 124 420 122 C540 112 640 76 700 60 L903 40 L903 300 L0 300 Z" fill="var(--footer)"/>
  </svg>
  <div class="abs emblem-dot"></div>
  <div class="abs emblem-name">KVR</div>

  <h3 class="abs col-title" style="left:102px">Quick Links</h3>
  <h3 class="abs col-title" style="left:250px">Investigation Request</h3>
  <h3 class="abs col-title" style="left:441px">Latest News</h3>
  <h3 class="abs col-title" style="left:638px">Contact Details</h3>
  <div class="abs rule" style="left:99px;top:1052px;width:124px"></div>
  <div class="abs rule" style="left:249px;top:1052px;width:170px"></div>
  <div class="abs rule" style="left:441px;top:1052px;width:170px"></div>
  <div class="abs rule" style="left:638px;top:1052px;width:165px"></div>

  <ul class="abs quick">
    <li>Home</li><li>About Us</li><li>Research</li><li>News</li><li>Videos</li><li>Contact Us</li>
  </ul>

  <div class="abs field" style="top:1060px;height:16px">Your Name</div>
  <div class="abs field" style="top:1081px;height:16px">Your Email</div>
  <div class="abs field" style="top:1102px;height:38px">Message</div>
  <div class="abs submit">Submit</div>

  <div class="abs news" style="top:1058px"><div class="date">25.05.2015</div><b>Lorem ipsum dolor</b> sit amet, consec te tuer adipi scing. Praesent vestibu.</div>
  <div class="abs rule" style="left:441px;top:1104px;width:170px"></div>
  <div class="abs news" style="top:1109px"><div class="date">25.05.2015</div><b>Lorem ipsum dolor</b> sit amet, consec te tuer adipi scing. Praesent vestibu.</div>
  <div class="abs" style="left:597px;top:1151px;width:11px;height:11px;background:var(--bone);color:#111;font-size:10px;line-height:10px;text-align:center;font-weight:700;border-radius:1px">+</div>

  <svg class="abs" style="left:634px;top:1061px" width="14" height="90" viewBox="0 0 14 90" aria-hidden="true">
    <path d="M7 2a5 5 0 0 0-5 5c0 4 5 9 5 9s5-5 5-9a5 5 0 0 0-5-5z" fill="#eee"/><circle cx="7" cy="7" r="2" fill="var(--footer)"/>
    <path d="M3 37c1-2 3-2 4 0l-1 2c1 2 2 3 4 4l2-1c2 1 2 3 0 4-4 2-10-5-9-9z" fill="#eee"/>
    <rect x="2" y="66" width="10" height="7" fill="#eee"/><path d="M2 66l5 4 5-4" stroke="var(--footer)" fill="none"/>
  </svg>
  <div class="abs contact" style="top:1060px">Sed diam nonummy euismod tincidu nt ut laor 12568</div>
  <div class="abs contact" style="top:1096px">Phone:(000)123-4567</div>
  <div class="abs contact" style="top:1122px">info@kvrparanormal.example</div>

  <div class="abs base"></div>
  <p class="abs copy">Copyright© 2015 KVR Paranormal Investigations. All rights reserved</p>
  <div class="abs social" style="left:734px;background:#3b5a9a"></div>
  <div class="abs social" style="left:760px;background:#3d8fd0"></div>
  <div class="abs social" style="left:786px;background:#e0751e"></div>
</div>
</body>
</html>
```